Attorney Website Design

I need a top quality attorney website layout designed. Here are some examples of what I feel are great websites:
http://www.brelmoradivorceattorney.example/
http://www.vethomirlawfirm.example/
http://www.plexfirm.example/
http://www.harrowgatecriminaldefensefirm.example/
http://www.qzfirm.example/
http://www.tolvermoorcriminaldefensefirm.example/
http://www.drennocriminalattorneys.example/
http://www.qzfirm.example/
What we like about these sites:
• The different layers
• Subtle designs, textures, curves
• 3 dimensional
• Floating effects
• Prominent phone number
• Location of Areas of Practice
• Request A Consultation Prominent
• Right side bar with practice areas
• Badges
• Clear Calls to Action
• Dynamic/Staying Top navigation when you scroll
The project will be for a home page and then also an interior page (should be similar to home page).
I want to make it understood I am looking for a design which is not a typical "template" site which I can find anywhere for $50. This budget and project is for a "Custom" website design. Please submit designs similar in quality to the samples links I have posted. Creativity is a MUST! The best way to explain this is, I want a design that I can feel it unique and original, not something that looks like 95% of all websites out there.
Owen
I just wanted everyone to know that so far I am not to pleased with any of the designs. I am not looking for cut/pasting of other peoples websites but ORIGINAL and CREATIVE work.
Industry/Entity Type
Attorney

```html
<!DOCTYPE html>
<html lang="en">
<head>
<meta charset="utf-8">
<title>Attorney – Home</title>
<link rel="stylesheet" href="https://fonts.googleapis.com/css2?family=Ubuntu:wght@300;400;500&family=PT+Sans:wght@400;700&display=swap">
<style>
  :root {
    --plum: #5b4c5a;
    --plum-dark: #463a46;
    --plum-deep: #3a2f39;
    --coral: #e85a55;
    --coral-soft: #d0605a;
    --ink: #333333;
    --body: #4a4a4a;
    --rule: #e4e4e4;
    --field-line: #cfcfcf;
    --footer: #2b2b2b;
    --footer-base: #232323;
    --white: #ffffff;
  }
  * { box-sizing: border-box; margin: 0; padding: 0; }
  html, body { width: 821px; height: 1200px; overflow: hidden; }
  body { position: relative; background: var(--white); font-family: "PT Sans", Arial, sans-serif; color: var(--body); }
  .abs { position: absolute; }

  /* Header */
  .site-header { position: absolute; left: 0; top: 0; width: 821px; height: 77px;
    background: linear-gradient(#665866, var(--plum)); border-top: 2px solid var(--coral); border-bottom: 3px solid var(--plum-deep); }
  .brand { position: absolute; left: 95px; top: 24px; font-family: "Ubuntu", sans-serif; font-weight: 400; font-size: 27px; letter-spacing: 1px; color: var(--white); }
  .call-box { position: absolute; left: 534px; top: -2px; width: 192px; height: 28px; background: var(--coral);
    color: var(--white); font-family: "Ubuntu", sans-serif; font-size: 13px; line-height: 28px; text-align: center; border-radius: 0 0 3px 3px; }
  .call-box strong { font-size: 18px; font-weight: 400; margin-left: 4px; }
  .main-nav { position: absolute; top: 34px; left: 383px; display: flex; font-family: Arial, sans-serif; font-size: 11px; color: var(--white); }
  .main-nav a { color: inherit; text-decoration: none; height: 29px; line-height: 29px; text-align: center; border-radius: 3px; }
  .main-nav .active { background: var(--plum-deep); width: 64px; }
  .main-nav .n-about { width: 80px; margin-left: 2px; }
  .main-nav .n-services { width: 80px; }
  .main-nav .n-blog { width: 60px; }
  .main-nav .n-contacts { width: 78px; }

  /* Hero */
  .hero { position: absolute; left: 0; top: 77px; width: 821px; height: 300px; overflow: hidden; }
  .hero-photo { position: absolute; inset: 0;
    background: radial-gradient(ellipse 260px 230px at 47% 45%, #f6efea 0%, #efdcd0 40%, rgba(232,150,120,0) 100%),
                linear-gradient(90deg, #c76a4c 0%, #e79a78 25%, #f4dccf 45%, #f4dccf 60%, #e9a07c 80%, #c5684b 100%); }
  .hero-card { position: absolute; left: 95px; top: 67px; width: 202px; height: 148px; border: 2px solid rgba(255,255,255,.85);
    background: rgba(255,255,255,.55); padding: 12px 0 0 20px; }
  .hero-card h1 { font-family: "Ubuntu", sans-serif; font-weight: 400; font-size: 29px; color: #1f1f1f; line-height: 34px; }
  .hero-card p { font-family: "Ubuntu", sans-serif; font-weight: 400; font-size: 22px; line-height: 29px; color: var(--coral-soft); }
  .btn-dark { display: inline-block; background: #2c2a2c; color: var(--white); font-size: 10px; text-align: center; border-radius: 3px; }
  .hero-card .btn-dark { position: absolute; left: 18px; top: 114px; width: 48px; height: 22px; line-height: 22px; }
  .hero-curve { position: absolute; left: 0; top: 0; }

  /* Welcome band */
  .welcome { position: absolute; left: 0; top: 371px; width: 821px; height: 138px; background: var(--plum); text-align: center; color: var(--white); }
  .welcome h2 { font-family: "Ubuntu", sans-serif; font-weight: 300; font-size: 23px; letter-spacing: .5px; margin-top: 14px; }
  .welcome p { width: 625px; margin: 8px auto 0; font-size: 9px; line-height: 11.5px; }
  .welcome .btn-dark { width: 70px; height: 25px; line-height: 25px; margin-top: 10px; }

  /* Content */
  .col-main { position: absolute; left: 95px; width: 410px; }
  .section-title { font-family: "Ubuntu", sans-serif; font-weight: 400; font-size: 19px; line-height: 23px; color: var(--ink); }
  .copy { font-size: 9px; line-height: 11.5px; color: var(--body); }
  .btn-coral { position: absolute; left: 95px; width: 53px; height: 25px; line-height: 25px; background: var(--coral); color: var(--white);
    font-size: 11px; text-align: center; border-radius: 3px; }
  .rule { position: absolute; left: 95px; width: 410px; height: 1px; background: var(--rule); }
  .case-photo { position: absolute; left: 95px; top: 912px; width: 170px; height: 105px; border-radius: 3px;
    background: linear-gradient(160deg, #6b4a2a 0%, #b88a52 40%, #e7d3ad 60%, #8c5f34 100%); }

  /* Sidebar */
  .panel { position: absolute; left: 541px; width: 185px; border: 1px solid #d7d7d7; border-radius: 4px; background: var(--white); }
  .panel-head { height: 30px; line-height: 30px; padding-left: 12px; color: var(--white); font-family: "Ubuntu", sans-serif; font-size: 17px; border-radius: 3px 3px 0 0; }
  .panel-email { top: 534px; height: 270px; }
  .panel-email .panel-head { background: var(--coral); }
  .field { position: absolute; left: 10px; width: 165px; border: 1px solid var(--field-line); border-radius: 5px; font-size: 9px; color: #666; padding: 8px 0 0 10px; }
  .btn-send { position: absolute; left: 10px; top: 229px; width: 56px; height: 28px; line-height: 28px; background: #262426; color: var(--white);
    font-family: Arial, sans-serif; font-weight: 700; font-size: 13px; text-align: center; border-radius: 4px; }
  .panel-practice { top: 823px; height: 226px; }
  .panel-practice .panel-head { background: var(--plum); }
  .practice-list { list-style: none; margin: 11px 0 0 10px; font-size: 10px; color: #444; }
  .practice-list li { height: 25.8px; line-height: 14px; padding-left: 13px; position: relative; }
  .practice-list li::before { content: ""; position: absolute; left: 0; top: 4px; border-left: 4px solid #444; border-top: 3px solid transparent; border-bottom: 3px solid transparent; }

  /* Footer */
  .site-footer { position: absolute; left: 0; top: 1088px; width: 821px; height: 112px; background: var(--footer-base); }
  .footer-nav { height: 55px; background: var(--footer); display: flex; justify-content: center; align-items: center; font-family: Arial, sans-serif; font-size: 10px; color: #cfcfcf; }
  .footer-nav span.sep { margin: 0 18px; }
  .copyright { text-align: center; font-family: Arial, sans-serif; font-size: 8px; color: #777; margin-top: 11px; }
</style>
</head>
<body>

<header class="site-header">
  <div class="brand">ATTORNEY</div>
  <div class="call-box">Call today: <strong>5550 182 4476</strong></div>
  <nav class="main-nav">
    <a class="active">HOME</a>
    <a class="n-about">ABOUT</a>
    <a class="n-services">SERVICES</a>
    <a class="n-blog">BLOG</a>
    <a class="n-contacts">CONTACTS</a>
  </nav>
</header>

<section class="hero">
  <div class="hero-photo" role="img" aria-label="Slideshow photo of a stressed client holding her head"></div>
  <div class="hero-card">
    <h1>PROVIDING</h1>
    <p>PERSONALIZED<br>SERVICES.</p>
    <span class="btn-dark">MORE</span>
  </div>
  <svg class="hero-curve" width="821" height="300" viewBox="0 0 821 300">
    <path d="M0 294 Q410 248 821 294 L821 300 L0 300 Z" fill="#5b4c5a"/>
    <circle cx="398" cy="281" r="5" fill="#6f626e"/>
    <circle cx="410" cy="281" r="5" fill="#e85a55"/>
    <circle cx="422" cy="281" r="5" fill="#6f626e"/>
  </svg>
</section>

<section class="welcome">
  <h2>WELCOME</h2>
  <p>Vivamus vehicula erat non mi vulputate, et dictum dui viverra. Phasellus sed erat felis. Nullam suscipit fermentum erat dictum eleifend. Vestibulum accumsan elit non nibh varius, quis malesuada arcu tristique. Etiam blandit augue ut iaculis vehicula. In ipsum purus, dictum ac metus vel, mattis tristique massa. Suspendisse ipsum odio, egestas dignissim ante ac, varius auctor dui. Donec commodo lacus eget porta cursus.</p>
  <span class="btn-dark">Know more</span>
</section>

<main>
  <h2 class="section-title col-main" style="top:532px;">About us</h2>
  <p class="copy col-main" style="top:562px;">Duis feugiat lobortis iaculis. Etiam aliquet, nisl ac porttitor fringilla, libero diam congue ipsum, sed porttitor risus tellus id magna. Nunc posuere, enim vitae vehicula sagittis, tellus nulla commodo turpis, id porttitor metus leo at turpis. Duis ac arcu semper, imperdiet dui non, iaculis massa. Donec pretium sodales erat quis fermentum. In eget augue sed magna scelerisque rhoncus nec vitae elit. In hendrerit metus sit amet ante iaculis.</p>
  <span class="btn-coral" style="top:631px;">More</span>
  <div class="rule" style="top:679px;"></div>

  <h2 class="section-title col-main" style="top:698px;">Realize your constitutional right with qualified legal help</h2>
  <p class="copy col-main" style="top:752px;">Consectetuer adipiscing elit, sed diam nonummy nibh euismod tincidunt ut laoreet dolore magna aliquam erat volutpat. Ut wisi enim ad minim veniam, quis nostrud exerci tation ullamcorper suscipit lobortis nisl ut aliquip ex ea commodo consequat. Duis autem vel eum iriure dolor in hendrerit in vulputate velit esse molestie consequat, vel illum dolo.</p>
  <span class="btn-coral" style="top:812px;">More</span>
  <div class="rule" style="top:860px;"></div>

  <h2 class="section-title col-main" style="top:875px;">Case Studies</h2>
  <div class="case-photo" role="img" aria-label="Photo of open law books on a shelf"></div>
  <p class="copy abs" style="left:276px; top:911px; width:205px; line-height:12.2px;">Aenean in lorem odio. Duis sodales a dolor non blandit. Vivamus rhoncus adipiscing malesuada. Phasellus scelerisque tincidunt condimentum. Praesent iaculis gravida consequat. Nullam ac interdum leo, eget placerat lacus. Quisque eget libero arcu. Suspendisse ultrices rutrum ipsum, quis fringilla sem scelerisque at. Pellentesque arcu mi, venenatis quis tempus a, semper condimentum dolor.</p>
</main>

<aside>
  <div class="panel panel-email">
    <div class="panel-head">Reach us by Email</div>
    <div class="field" style="top:48px; height:30px;">Name:</div>
    <div class="field" style="top:84px; height:30px;">Email:</div>
    <div class="field" style="top:119px; height:30px;">Address:</div>
    <div class="field" style="top:154px; height:68px;">Massage:</div>
    <div class="btn-send">SEND</div>
  </div>

  <div class="panel panel-practice">
    <div class="panel-head">Area of Practice</div>
    <ul class="practice-list">
      <li>Criminal Defence</li>
      <li>Criminal Law Info</li>
      <li>Types of Crimes</li>
      <li>Driving Under the Influence</li>
      <li>Drug Crimes</li>
      <li>Theft Crimes</li>
      <li>Voilent Crime</li>
    </ul>
  </div>
</aside>

<footer class="site-footer">
  <nav class="footer-nav">
    <span>Home</span><span class="sep">|</span>
    <span>About</span><span class="sep">|</span>
    <span>Services</span><span class="sep">|</span>
    <span>Blog</span><span class="sep">|</span>
    <span>Contacts</span>
  </nav>
  <p class="copyright">www.attorney.example All Rights Reserved.</p>
</footer>

</body>
</html>
```